Surgical Sales Presentation Folder

Presentation folder; three panel; custom cutouts; Six 8.5 x 11 full color sales sheets to be bound into presentation folder; 5 full color sales sheets, stepped, longest being 8.5 x 11.
We are Brantley Surgical Group and we are a surgical company that supports physicians who wish to become surgeons. Our clients are Physicians. As such, the design needs to be very professional.
I have included a list of photos and a letter describing what we like about each photo. I have included the verbiage with page identifiers. If this makes scene, please feel free to add photos to the inside of the folder or I can provide you with examples that we think are similar to what we are looking for.
Updates
Target Market(s)
Doctors who want to be surgeons.
Industry/Entity Type
Sales
Requirements
Must have
- Presentation folder; three panel; custom cutouts; Six 8.5 x 11 full color sales sheets to be bound into presentation folder; 5 full color sales sheets, stepped, longest being 8.5 x 11.

```html
<!DOCTYPE html>
<html lang="en">
<head>
<meta charset="utf-8">
<title>Barriers to Building a New Surgical Practice — Brantley Surgical Group</title>
<link href="https://fonts.googleapis.com/css2?family=Arimo:wght@400;700&display=swap" rel="stylesheet">
<style>
  :root {
    --brand-blue: #1b8ecb;
    --text-dark: #1e1e1e;
    --page-white: #ffffff;
    --frame-grey: #d6d6d6;
    --footer-dark: #1c1c1c;
    --footer-mid: #2e2e2e;
    --footer-text: #cfd6dc;
    --photo-light: #d9c9ab;
    --photo-dark: #3a2e22;
  }
  * { margin: 0; padding: 0; box-sizing: border-box; }
  html, body { width: 927px; height: 1200px; overflow: hidden; background: var(--frame-grey); }
  .sheet {
    position: relative;
    width: 927px;
    height: 1200px;
    background: var(--page-white);
    border: 14px solid var(--frame-grey);
    font-family: "Arimo", Arial, sans-serif;
    color: var(--text-dark);
  }
  .sheet-title {
    position: absolute;
    left: 32px; top: 58px;
    width: 660px;
    font-size: 33px;
    line-height: 40px;
    font-weight: 700;
    color: var(--brand-blue);
  }
  .emblem {
    position: absolute;
    left: 728px; top: 24px;
    width: 116px; height: 174px;
    border-radius: 6px;
    background: linear-gradient(180deg, #bfe3f5 0%, #4aa6d6 55%, #a9b3ba 100%);
  }
  .hero-photo {
    position: absolute;
    left: 422px; top: 195px;
    width: 422px; height: 618px;
    background: radial-gradient(circle at 50% 45%, var(--photo-light) 0%, #9c8466 45%, var(--photo-dark) 100%);
  }
  .section { position: absolute; left: 36px; }
  .section-heading {
    font-size: 21px;
    line-height: 23px;
    font-weight: 700;
    color: var(--brand-blue);
    text-transform: uppercase;
  }
  .section-body {
    font-size: 17px;
    line-height: 21.5px;
    font-weight: 700;
    color: var(--text-dark);
  }
  .section--time { top: 192px; width: 372px; }
  .section--finance { top: 572px; width: 372px; }
  .section--peace { top: 837px; width: 840px; }
  .section--finance .section-heading { width: 230px; }
  .footer-band {
    position: absolute;
    left: 0; right: 0; top: 1062px;
    height: 88px;
    background: linear-gradient(180deg, var(--footer-mid) 0%, var(--footer-dark) 100%);
    display: flex;
    align-items: center;
    padding-left: 32px;
    gap: 14px;
  }
  .footer-mark {
    width: 46px; height: 46px;
    border-radius: 50%;
    background: var(--brand-blue);
  }
  .footer-name {
    font-size: 30px;
    font-weight: 700;
    color: var(--footer-text);
    letter-spacing: 0.5px;
  }
</style>
</head>
<body>
  <main class="sheet">
    <h1 class="sheet-title">Barriers to Building a New Surgical Practice</h1>
    <div class="emblem" role="img" aria-label="Blue winged medical staff emblem"></div>
    <div class="hero-photo" role="img" aria-label="Photograph of a spiralling antique clock face with Roman numerals"></div>

    <section class="section section--time">
      <h2 class="section-heading">Time</h2>
      <p class="section-body">Few physicians in the medical field can justify the time commitment required to develop and grow a secondary practice. This type of undertaking frequently requires full-time obligation. Clearly, this level of commitment is at best, prohibitive due to the full time commitment of their current practice. Also, the demands of a single practice frequently keep many physicians away from their loved ones longer and more frequently then originally anticipated. So for most, the addition of a second practice means giving up any time then is available.</p>
    </section>

    <section class="section section--finance">
      <h2 class="section-heading">Financial Considerations</h2>
      <p class="section-body">Time is money, and any time spent away from your current practice is money lost. This is the reality of the medical physician; if you are not there grinding away, you don’t make money. For most physicians, this reality makes it almost impossible to start and grow a surgical practice while maintaining their medical practice.</p>
    </section>

    <section class="section section--peace">
      <h2 class="section-heading">Peace of Mind</h2>
      <p class="section-body">Along with the already-considerable investments of time and finances, significant mental energy is needed to learn and hone a new craft, while addressing the thousand other details and issues clamor for your attention, all while maintaining your current practice. It’s not surprising that the stress level also increases exponentially.</p>
    </section>

    <footer class="footer-band">
      <span class="footer-mark"></span>
      <span class="footer-name">Brantley Surgical Group</span>
    </footer>
  </main>
</body>
</html>
```